Friendly website/webshop needed for small family store

Hello .. I really need a website that is easy to use as I have no experience with this at all. ..
My shop is called hollowmoss and I had a fantastic logo from plume yard - I asked for something mid century modern and I love it. I will attach . There might be some development around the logo now for various paraphernalia ( stickers , printed tissue paper carrier bags etc.. ) I would also like some sort of help with a slogan such as 'sing your prettiest song' as in,  live your best life etc..  but I'm not sure if this is a little trite .... ? but it would be nice to link the hollowmoss with a little Motto.    If I need to pay extra for this - please could you let me know ... I'm happy to add on payment ..
As you can see the only LOGO colours really are grey black and orange .. so I would like some ideas to expand on the bird  to bring in some more colours.....  the tag line flower.children.home I would like to drop..
* the original brief included flowers on the tag line  because at the time we were also a florist . we now just sell dried flowers
My shop is in the beautiful town of Malvern, we have lots of tourist that come to walk the hills and enjoy nature - it's a family and dog friendly sort of town and we are a dog and family friendly sort of shop :-) It's a relaxed space that focuses on beautiful handmade items such as baskets & wooden utensils  from Africa, textiles from India and ceramics from France, Portugal and Italy.  We have a lovely section for children that sells beautiful soft toys from Tevare Lusin and the wonderful mice family and bunnies from Orvasi.
We stock TOLVA homeware which is lovely and earthy and natural.
We would like to communicate the value of buying thoughtfully  and conscientiously, of building a beautiful home whilst investing in & supporting makers world wide. We don't sell anything that can't be repurposed, recycled etc..
Thank you

```html
<!DOCTYPE html>
<html lang="en">
<head>
<meta charset="utf-8">
<title>hollowmoss — handmade home, children &amp; dried flowers</title>
<link href="https://fonts.googleapis.com/css2?family=Bungee&family=Jost:ital,wght@0,300;0,400;0,500;0,600;1,300;1,400&display=swap" rel="stylesheet">
<style>
:root{
  --slate:#6f7c9c;
  --rose:#cd8478;
  --teal:#7ab8c9;
  --ink:#1c1c1c;
  --text:#6b6b6b;
  --paper:#f4f4f4;
  --white:#ffffff;
  --black:#000000;
  --star:#f2c14e;
}
*{box-sizing:border-box;margin:0;padding:0}
html,body{width:1200px;height:3275px;overflow:hidden}
body{position:relative;background:var(--white);font-family:"Jost",sans-serif;color:var(--text)}
.abs{position:absolute}
a{color:inherit;text-decoration:none}

/* top bar */
.topbar{top:0;left:0;width:1200px;height:60px;background:var(--white)}
.topbar-item{display:flex;align-items:center;gap:12px;font-weight:500;font-size:17px;color:var(--ink);top:14px}
.round-icon{width:32px;height:32px;border-radius:50%;background:var(--rose);display:flex;align-items:center;justify-content:center}
.nav{top:60px;left:0;width:1200px;height:41px;background:var(--slate)}
.nav a{position:absolute;top:11px;color:var(--white);font-size:14px;font-weight:400}
.logo-tab{top:0;left:0;width:1200px;height:125px}
.logo-name{top:74px;left:0;width:1200px;text-align:center;font-weight:600;font-size:24px;color:var(--ink);letter-spacing:.5px}
.logo-dot{top:20px;left:578px;width:44px;height:44px;border-radius:50%;background:var(--slate)}

/* hero */
.hero-photo{top:100px;left:0;width:1200px;height:600px;
  background:
    radial-gradient(ellipse 260px 200px at 90px 260px,rgba(38,52,30,.9),transparent 70%),
    radial-gradient(ellipse 240px 260px at 1080px 330px,rgba(70,72,60,.85),transparent 70%),
    radial-gradient(ellipse 320px 230px at 760px 380px,rgba(96,84,72,.9),transparent 70%),
    radial-gradient(ellipse 150px 200px at 680px 220px,rgba(120,104,86,.85),transparent 70%),
    radial-gradient(ellipse 300px 120px at 980px 200px,rgba(120,140,120,.6),transparent 70%),
    radial-gradient(ellipse 320px 140px at 200px 500px,rgba(140,80,62,.7),transparent 70%),
    radial-gradient(ellipse 420px 120px at 600px 560px,rgba(80,80,82,.9),transparent 70%),
    linear-gradient(180deg,#7a9cc8 0%,#a7bed6 30%,#5d6a4c 55%,#3e4234 80%,#4a4440 100%)}
.hero-photo::after{content:"";position:absolute;inset:0;background:linear-gradient(90deg,rgba(0,0,0,.28) 0%,rgba(0,0,0,.1) 45%,transparent 70%)}
.hero-title{top:236px;left:143px;font-family:"Bungee",sans-serif;font-size:36px;color:var(--white);letter-spacing:.5px}
.hero-title span{color:var(--rose)}
.hero-text{top:298px;left:143px;width:390px;font-size:16px;line-height:26px;color:var(--white)}
.btn{display:flex;align-items:center;justify-content:center;gap:8px;background:var(--rose);color:var(--white);font-weight:600;border-radius:4px;text-transform:uppercase}
.hero-btn{top:370px;left:143px;width:168px;height:44px;font-size:15px}
.hero-shape{top:540px;left:0;width:1200px;height:160px}

/* about */
.about-block{top:979px;left:127px;width:226px;height:193px;background:var(--teal)}
.about-photo{top:757px;left:149px;width:415px;height:394px;border-radius:60px 0 80px 0;
  background:
    radial-gradient(ellipse 90px 60px at 60px 250px,rgba(180,90,110,.55),transparent 70%),
    radial-gradient(ellipse 120px 70px at 300px 300px,rgba(150,120,90,.7),transparent 70%),
    radial-gradient(ellipse 110px 120px at 340px 190px,rgba(120,140,170,.55),transparent 70%),
    linear-gradient(180deg,#eef0f3 0%,#e6e9ee 12%,#8b96a3 16%,#c9ced6 26%,#f3f4f6 34%,#d7dadf 55%,#9aa0a4 72%,#6e6b68 84%,#5a5856 100%)}
.section-title{font-family:"Bungee",sans-serif;font-size:30px;color:var(--ink)}
.about-title{top:804px;left:623px}
.accent-teal{color:var(--teal)}
.accent-rose{color:var(--rose)}
.about-text{top:858px;left:623px;width:434px;font-size:14px;line-height:24px;font-weight:300;text-align:justify}
.about-text p+p{margin-top:10px}
.about-btn{top:1055px;left:623px;width:142px;height:45px;font-size:13px}

/* products */
.products{top:1290px;left:0;width:1200px;height:605px;background:var(--paper)}
.products-title{top:1360px;left:0;width:1200px;text-align:center}
.card{top:1444px;width:212px}
.card-img{width:212px;height:246px;border-radius:8px}
.card-name{margin-top:22px;font-size:16px;color:var(--ink)}
.stars{margin-top:6px;font-size:11px;color:var(--star);letter-spacing:1px}
.stars span{color:#b5b5b5;letter-spacing:0;margin-left:6px}
.price{margin-top:6px;font-size:15px;font-weight:500;color:var(--rose)}
.price s{font-size:11px;color:#a5a5a5;margin-right:8px;font-weight:400}
.dots{top:1819px;left:563px;display:flex;gap:8px}
.dots i{width:12px;height:12px;border-radius:50%;background:#b3b3b3;display:block}
.dots i:first-child{background:var(--rose)}
.img-ceramics{background:
  radial-gradient(ellipse 60px 80px at 170px 130px,#f1d21a,transparent 75%),
  radial-gradient(ellipse 50px 60px at 70px 60px,#efc928,transparent 75%),
  radial-gradient(ellipse 45px 50px at 30px 150px,#e6a8c6,transparent 75%),
  radial-gradient(ellipse 60px 50px at 60px 220px,#efe6cc,transparent 75%),
  radial-gradient(ellipse 50px 40px at 20px 30px,#d9372f,transparent 75%),
  radial-gradient(ellipse 40px 40px at 200px 30px,#7d3b7a,transparent 75%),
  linear-gradient(135deg,#c94036,#d7a24c 45%,#b9927a 75%,#cfb493)}
.img-wood{background:
  radial-gradient(ellipse 70px 50px at 50px 150px,#6c8a78,transparent 75%),
  radial-gradient(ellipse 80px 60px at 140px 80px,#c9a37c,transparent 75%),
  radial-gradient(ellipse 70px 40px at 90px 215px,#a5583a,transparent 75%),
  radial-gradient(ellipse 60px 70px at 60px 60px,#7a3f2f,transparent 75%),
  linear-gradient(135deg,#5e3a26,#a47a56 45%,#6b4430 75%,#8d6448)}
.img-knit{background:
  radial-gradient(ellipse 55px 45px at 155px 70px,#e2902e,transparent 75%),
  radial-gradient(ellipse 45px 40px at 55px 60px,#3f8a98,transparent 75%),
  radial-gradient(ellipse 50px 55px at 150px 160px,#2f6e7c,transparent 75%),
  radial-gradient(ellipse 40px 50px at 55px 160px,#c98a3a,transparent 75%),
  radial-gradient(ellipse 110px 30px at 106px 225px,#6a4a30,transparent 80%),
  linear-gradient(135deg,#3a2e24,#6e5238 50%,#3b2d22)}
.img-flowers{background:
  radial-gradient(ellipse 90px 70px at 106px 70px,#fbfaf6,transparent 75%),
  radial-gradient(ellipse 70px 60px at 106px 185px,#b6946f,transparent 75%),
  radial-gradient(ellipse 40px 30px at 180px 215px,#f1efe9,transparent 80%),
  radial-gradient(ellipse 60px 50px at 60px 90px,#9aa080,transparent 75%),
  linear-gradient(180deg,#ecebe6,#e4e2db 60%,#e7e4dd)}

/* testimonials */
.testimonials{top:1894px;left:0;width:1200px;height:331px;
  background:
    radial-gradient(ellipse 260px 180px at 1120px 130px,rgba(70,78,100,.7),transparent 70%),
    radial-gradient(ellipse 260px 160px at 80px 200px,rgba(72,80,104,.6),transparent 70%),
    radial-gradient(ellipse 500px 90px at 600px 300px,rgba(86,92,118,.6),transparent 70%),
    radial-gradient(ellipse 400px 80px at 600px 40px,rgba(140,150,176,.5),transparent 70%),
    linear-gradient(180deg,#7a87a5 0%,#7382a1 50%,#66728f 100%)}
.test-title{top:1962px;left:366px;font-family:"Bungee",sans-serif;font-size:27px;color:var(--white)}
.test-photo{top:2016px;left:222px;width:88px;height:88px;transform:rotate(45deg);border-radius:6px;
  background:radial-gradient(circle at 50% 55%,#caa88e 0,#b79a82 22%,#d8d8d8 40%,#c6c6c6 100%)}
.test-quote{top:2025px;left:366px;width:620px;font-size:15px;line-height:25px;font-style:italic;font-weight:300;color:var(--white)}
.test-name{top:2138px;left:366px;font-size:15px;color:var(--white)}
.test-name small{font-size:10px}
.qmark{font-family:Georgia,serif;font-size:60px;color:rgba(255,255,255,.35);line-height:1}

/* services */
.services-title{top:2303px;left:0;width:1200px;text-align:center}
.service{top:2383px;width:285px;height:231px;background:var(--white);box-shadow:0 2px 14px rgba(0,0,0,.08);text-align:center}
.service-icon{margin:18px auto 0;width:76px;height:76px;border-radius:50%;background:var(--rose);display:flex;align-items:center;justify-content:center}
.service h3{margin-top:22px;font-size:17px;font-weight:400;color:var(--ink)}
.service p{margin:12px auto 0;width:225px;font-size:12px;line-height:23px;font-weight:300}

/* footer */
.footer-shape{top:2670px;left:0;width:1200px;height:160px}
.footer{top:2828px;left:0;width:1200px;height:447px;background:var(--black)}
.offer-title{top:2813px;left:0;width:1200px;text-align:center;font-size:33px;font-weight:400;color:var(--white)}
.offer-sub{top:2862px;left:0;width:1200px;text-align:center;font-size:11px;color:var(--white)}
.email{top:2908px;left:325px;width:550px;height:44px;background:var(--white);display:flex;align-items:center;justify-content:space-between;padding:0 20px 0 17px;font-size:10px;color:#777}
.foot-head{font-size:17px;font-weight:500;color:var(--white)}
.foot-menu{top:2990px;left:144px}
.foot-menu li{list-style:none;font-size:11px;color:var(--white);line-height:26px}
.foot-menu ul{margin-top:10px}
.foot-contact{top:2990px;left:425px}
.contact-row{display:flex;gap:16px;margin-top:12px;font-size:11px;line-height:21px;color:var(--white);width:220px}
.contact-row svg{flex:none;margin-top:4px}
.foot-about{top:2990px;left:775px;width:252px}
.foot-about p{margin-top:14px;font-size:10px;line-height:25px;color:var(--white)}
.divider{top:3196px;left:144px;width:912px;height:1px;background:#333}
.copyright{top:3219px;left:144px;font-size:11px;color:var(--white)}
.copyright u{text-underline-offset:2px}
.socials{top:3212px;left:946px;display:flex;gap:7px}
.socials i{width:31px;height:31px;border-radius:50%;background:var(--rose);display:block}
</style>
</head>
<body>

<header class="abs topbar">
  <div class="abs topbar-item" style="left:144px">
    <span class="round-icon"><svg width="16" height="16" viewBox="0 0 24 24" fill="#fff"><path d="M6.6 10.8a15 15 0 0 0 6.6 6.6l2.2-2.2a1 1 0 0 1 1-.25 11.4 11.4 0 0 0 3.6.57 1 1 0 0 1 1 1V20a1 1 0 0 1-1 1A17 17 0 0 1 3 4a1 1 0 0 1 1-1h3.5a1 1 0 0 1 1 1c0 1.25.2 2.45.57 3.57a1 1 0 0 1-.25 1z"/></svg></span>
    +1-888-888-8888
  </div>
  <div class="abs topbar-item" style="left:362px">
    <span class="round-icon"><svg width="16" height="16" viewBox="0 0 24 24" fill="#fff"><path d="M3 4h3l2.4 10h10l2-7H8" stroke="#fff" stroke-width="2" fill="none"/><circle cx="9.5" cy="19" r="1.6"/><circle cx="17" cy="19" r="1.6"/></svg></span>
    My Cart
  </div>
  <div class="abs topbar-item" style="left:743px;font-size:14px">
    <span class="round-icon"><svg width="14" height="16" viewBox="0 0 24 24" fill="#fff"><path d="M12 2a7 7 0 0 0-7 7c0 5 7 13 7 13s7-8 7-13a7 7 0 0 0-7-7zm0 9.5A2.5 2.5 0 1 1 12 6.5a2.5 2.5 0 0 1 0 5z"/></svg></span>
    Lorem ipsum dolor sit amet 651
  </div>
  <svg class="abs" style="top:22px;left:1041px" width="14" height="14" viewBox="0 0 24 24" fill="none" stroke="#1c1c1c" stroke-width="3"><circle cx="10" cy="10" r="7"/><path d="M15 15l7 7"/></svg>
</header>

<nav class="abs nav">
  <a href="#" style="left:144px">Home</a>
  <a href="#" style="left:245px">About</a>
  <a href="#" style="left:347px">Our Products</a>
  <a href="#" style="left:739px">Gallery</a>
  <a href="#" style="left:850px">Place an Order</a>
  <a href="#" style="left:1008px">Contact</a>
</nav>

<div class="abs hero-photo" role="img" aria-label="Hillside town view with a stone priory tower, trees and a street lamp"></div>
<svg class="abs logo-tab" viewBox="0 0 1200 125"><polygon points="490,0 710,0 694,122 506,122" fill="#fff"/></svg>
<span class="abs logo-dot"></span>
<div class="abs logo-name">hollowmoss</div>

<h1 class="abs hero-title">WELCOME TO HOLLOW<span>MOSS</span></h1>
<p class="abs hero-text">Lorem ipsum dolor sit amet, consectetur adipiscing elit, sed do eiusmod tempor incididunt ut labore.</p>
<a href="#" class="abs btn hero-btn">Shop Now
  <svg width="14" height="14" viewBox="0 0 24 24"><circle cx="12" cy="12" r="11" fill="#fff"/><path d="M10 7l5 5-5 5" stroke="#cd8478" stroke-width="3" fill="none"/></svg></a>
<svg class="abs hero-shape" viewBox="0 0 1200 160">
  <polygon points="0,15 600,100 1200,15 1200,51 636,118 600,156 564,118 0,51" fill="#6f7c9c"/>
  <polygon points="0,51 564,118 600,156 636,118 1200,51 1200,160 0,160" fill="#fff"/>
  <path d="M593 126l7 7 7-7" stroke="#fff" stroke-width="2.5" fill="none"/>
</svg>

<div class="abs about-block"></div>
<div class="abs about-photo" role="img" aria-label="Shop front with white window frames and baskets on the pavement"></div>
<h2 class="abs section-title about-title">ABOUT <span class="accent-teal">US</span></h2>
<div class="abs about-text">
  <p>Lorem ipsum dolor sit amet, consectetur adipiscing elit, sed do eiusmod tempor incididunt ut labore et dolore magna aliqua. Ut enim ad minim veniam, quis nostrud exercitation ullamco laboris nisi ut aliquip ex ea commodo consequat. Duis aute irure dolor in reprehenderit.</p>
  <p>Sed ut perspiciatis unde omnis iste natus error sit voluptatem accusantium doloremque laudantium, totam rem aperiam, eaque ipsa quae ab illo inventore veritatis et quasi architecto beatae.</p>
</div>
<a href="#" class="abs btn about-btn">Read More
  <svg width="13" height="13" viewBox="0 0 24 24"><circle cx="12" cy="12" r="11" fill="#fff"/><path d="M10 7l5 5-5 5" stroke="#cd8478" stroke-width="3" fill="none"/></svg></a>

<section class="abs products"></section>
<h2 class="abs section-title products-title"><span class="accent-teal">OUR</span> PRODUCTS</h2>

<article class="abs card" style="left:145px">
  <div class="card-img img-ceramics" role="img" aria-label="Colourful glazed ceramic jugs and cups"></div>
  <div class="card-name">Product Name</div>
  <div class="stars">★★★★★<span>(384)</span></div>
  <div class="price"><s>$20.00</s>$16.00</div>
</article>
<article class="abs card" style="left:377px">
  <div class="card-img img-wood" role="img" aria-label="Carved wooden bowls and utensils"></div>
  <div class="card-name">Product Name</div>
  <div class="stars">★★★★★<span>(384)</span></div>
  <div class="price"><s>$20.00</s>$16.00</div>
</article>
<article class="abs card" style="left:609px">
  <div class="card-img img-knit" role="img" aria-label="Knitted soft toys in woolly hats"></div>
  <div class="card-name">Product Name</div>
  <div class="stars">★★★★★<span>(384)</span></div>
  <div class="price"><s>$20.00</s>$16.00</div>
</article>
<article class="abs card" style="left:841px">
  <div class="card-img img-flowers" role="img" aria-label="Dried white flowers in a woven vase"></div>
  <div class="card-name">Product Name</div>
  <div class="stars">★★★★★<span>(384)</span></div>
  <div class="price"><s>$20.00</s>$16.00</div>
</article>
<div class="abs dots"><i></i><i></i><i></i><i></i></div>

<section class="abs testimonials" role="img" aria-label="Misty hills at dusk behind a blue overlay"></section>
<svg class="abs" style="top:2043px;left:80px" width="20" height="34" viewBox="0 0 20 34"><path d="M17 3L4 17l13 14" stroke="#fff" stroke-width="4" fill="none"/></svg>
<svg class="abs" style="top:2043px;left:1100px" width="20" height="34" viewBox="0 0 20 34"><path d="M3 3l13 14L3 31" stroke="#fff" stroke-width="4" fill="none"/></svg>
<h2 class="abs test-title">CUSTOMER TESTIMONIALS</h2>
<div class="abs test-photo" role="img" aria-label="Portrait of a smiling customer"></div>
<span class="abs qmark" style="top:2002px;left:326px">“</span>
<p class="abs test-quote">Sed ut perspiciatis unde omnis iste natus error sit voluptatem accusantium doloremque laudantium, totam rem aperiam, eaque ipsa quae ab illo inventore veritatis et quasi architecto beatae vitae dicta sunt explicabo. Duis aute irure dolor in reprehenderit in voluptate velit esse cillum dolore eu fugiat nulla pariatur deserunt mollit id est laborum.</p>
<span class="abs qmark" style="top:2098px;left:662px">”</span>
<div class="abs test-name">Wren Halloway - <small>Lorem Ipsum</small></div>

<h2 class="abs section-title services-title">OUR <span class="accent-teal">SERVICES</span></h2>
<div class="abs service" style="left:145px">
  <div class="service-icon"><svg width="38" height="38" viewBox="0 0 24 24" fill="none" stroke="#fff" stroke-width="1.4"><path d="M6.6 10.8a15 15 0 0 0 6.6 6.6l2.2-2.2 4.6 1.4V20A17 17 0 0 1 4 4h3.5l1.4 4.6z"/></svg></div>
  <h3>24/hr Contact</h3>
  <p>Lorem ipsum dolor sit amet, consectetur adipiscing elit, sed do</p>
</div>
<div class="abs service" style="left:457px">
  <div class="service-icon"><svg width="38" height="38" viewBox="0 0 24 24" fill="none" stroke="#fff" stroke-width="1.4"><rect x="5" y="4" width="14" height="17" rx="1"/><path d="M9 3h6v3H9zM8 10h2M12 10h4M8 14h2M12 14h4M8 18h2M12 18h4"/></svg></div>
  <h3>Place an Order</h3>
  <p>Lorem ipsum dolor sit amet, consectetur adipiscing elit, sed do</p>
</div>
<div class="abs service" style="left:769px">
  <div class="service-icon"><svg width="38" height="38" viewBox="0 0 24 24" fill="none" stroke="#fff" stroke-width="1.4"><circle cx="14" cy="10" r="7"/><path d="M9 15l-6 6M12 8a2 2 0 1 1 2.5 2c-.5.2-.5.8-.5 1.5M14 13.5v.5"/></svg></div>
  <h3>General Inquiries</h3>
  <p>Lorem ipsum dolor sit amet, consectetur adipiscing elit, sed do</p>
</div>

<footer class="abs footer"></footer>
<svg class="abs footer-shape" viewBox="0 0 1200 160">
  <polygon points="0,115 566,40 600,6 634,40 1200,115 1200,160 0,160" fill="#6f7c9c"/>
  <polygon points="0,152 600,72 1200,152 1200,160 0,160" fill="#000"/>
  <path d="M593 38l7-7 7 7" stroke="#fff" stroke-width="2.5" fill="none"/>
</svg>
<h2 class="abs offer-title">GET 20% OFF YOUR FIRST ORDER</h2>
<p class="abs offer-sub">Join our email list for exclusive offers and the latest news.</p>
<div class="abs email">Email Address
  <svg width="16" height="10" viewBox="0 0 16 10"><path d="M0 5h14M10 1l4 4-4 4" stroke="#cd8478" stroke-width="1.6" fill="none"/></svg></div>

<div class="abs foot-menu">
  <div class="foot-head">Menu</div>
  <ul><li>Home</li><li>About</li><li>Products</li><li>Gallery</li><li>Place on Order</li><li>Contact</li></ul>
</div>
<div class="abs foot-contact">
  <div class="foot-head">Contact Us</div>
  <div class="contact-row"><svg width="12" height="13" viewBox="0 0 24 24" fill="#cd8478"><path d="M12 2a7 7 0 0 0-7 7c0 5 7 13 7 13s7-8 7-13a7 7 0 0 0-7-7zm0 9.5A2.5 2.5 0 1 1 12 6.5a2.5 2.5 0 0 1 0 5z"/></svg><span>Lorem ipsum dolor sit amet, consectetur 651</span></div>
  <div class="contact-row"><svg width="13" height="11" viewBox="0 0 24 20" fill="#cd8478"><path d="M2 2h20v16H2z"/><path d="M2 3l10 8 10-8" stroke="#000" stroke-width="2" fill="none"/></svg><span>info@hollowmoss.com</span></div>
  <div class="contact-row"><svg width="12" height="12" viewBox="0 0 24 24" fill="#cd8478"><path d="M6.6 10.8a15 15 0 0 0 6.6 6.6l2.2-2.2 5.6 1.3V21A18 18 0 0 1 3 3h4.5l1.3 5.6z"/></svg><span>+1-888-888-8888</span></div>
  <div class="contact-row"><svg width="12" height="12" viewBox="0 0 24 24" fill="none" stroke="#cd8478" stroke-width="2.5"><circle cx="12" cy="12" r="10"/><path d="M12 6v6l4 2"/></svg><span>Live Chat Every Day 8am- 9pm</span></div>
</div>
<div class="abs foot-about">
  <div class="foot-head">Sed Do amet</div>
  <p>Lorem ipsum dolor sit amet, consectetur adipiscing elit, sed do eiusmod tempor incididunt ut labore et dolore magna aliqua. Ut enim ad minim veniam, quis nostrud exercitation ullamco laboris nisi ut aliquip ex ea commodo consequat.</p>
</div>
<div class="abs divider"></div>
<div class="abs copyright">Copyright© 2024 &nbsp;<u>hollowmoss</u> &nbsp;| &nbsp;All Rights Reserved</div>
<div class="abs socials"><i></i><i></i><i></i></div>

</body>
</html>
```